Book dust cover- front and back- 5.5x 8.5, white back ground, simple, testimonial on the back (just use sample words) price, qr code and picture of author. Front will include title and tagline
Tagline- The 7 Mindsets to Overcome Life's Challenges
Sorry, it didn't ask me specifically for everything.
Title: Walking Into Amber Light
Tagline: Seven Steady Habits to Rise Above Hard Seasons
Christian based- I use scripture and science to prove each mindset
No pink or girly looks
I like the covers like: Derek T Halloway's Books, Ironwilled, Fig and Kettle (words with little imagery- unless it really makes sense)
Females- 25-65
Christian

```html
<!DOCTYPE html>
<html lang="en">
<head>
<meta charset="utf-8">
<title>Walking Into Amber Light — Book Cover</title>
<link rel="stylesheet" href="https://fonts.googleapis.com/css2?family=Bebas+Neue&family=Lato:wght@400&family=Open+Sans:ital,wght@0,400;1,400&family=Playfair+Display:ital@1&display=swap">
<style>
  :root {
    --cover-blue: #27528a;
    --ink-blue: #22477c;
    --gold-light: #ffe21a;
    --gold-mid: #fbc711;
    --gold-deep: #efa205;
    --white: #ffffff;
  }
  * { margin: 0; padding: 0; box-sizing: border-box; }
  html, body { width: 1200px; height: 866px; overflow: hidden; background: var(--cover-blue); }
  .cover { position: relative; width: 1200px; height: 866px; background: var(--cover-blue); color: var(--white); }

  .display { font-family: "Bebas Neue", "Oswald", sans-serif; line-height: 1; position: absolute; left: 0; right: 0; text-align: center; white-space: nowrap; }
  .gold {
    background: linear-gradient(160deg, var(--gold-light) 0%, var(--gold-mid) 55%, var(--gold-deep) 100%);
    -webkit-background-clip: text; background-clip: text; color: transparent;
  }
  .connector { position: absolute; left: 0; right: 0; display: flex; align-items: center; justify-content: center; font-family: "Playfair Display", Georgia, serif; font-style: italic; }
  .connector .rule { height: 4px; background: var(--white); clip-path: polygon(0 50%, 100% 0, 100% 100%); }
  .connector .rule.right { clip-path: polygon(0 0, 100% 50%, 0 100%); }

  /* Back cover */
  .back { position: absolute; left: 0; top: 0; width: 560px; height: 866px; }
  .back-title { position: absolute; left: 160px; width: 240px; top: 0; height: 300px; }
  .back-divider { position: absolute; left: 16px; top: 299px; width: 534px; height: 4px; background: var(--white); }
  .blurb { position: absolute; left: 30px; top: 332px; width: 500px; font-family: "Lato", sans-serif; font-size: 15px; line-height: 18.8px; text-align: center; hyphens: auto; -webkit-hyphens: auto; }
  .blurb p + p { margin-top: 18.8px; }
  .back-band { position: absolute; left: 0; top: 676px; width: 560px; height: 160px; background: linear-gradient(100deg, var(--gold-mid), var(--gold-light) 40%, var(--gold-mid)); }
  .price-panel { position: absolute; left: 330px; top: 718px; width: 204px; height: 119px; background: var(--white); }

  /* Spine */
  .spine { position: absolute; left: 560px; top: 0; width: 80px; height: 866px; }
  .spine-text { position: absolute; left: 19px; writing-mode: vertical-rl; font-family: "Bebas Neue", sans-serif; font-size: 52px; line-height: 42px; white-space: nowrap; color: var(--white); }
  .spine-title { top: 74px; }
  .spine-title em { font-family: "Playfair Display", serif; font-size: 26px; }
  .spine-author { top: 568px; font-size: 56px; }

  /* Front cover */
  .front { position: absolute; left: 640px; top: 0; width: 560px; height: 866px; }
  .front-title { position: absolute; left: 0; width: 560px; top: 0; height: 560px; }
  .tagline { position: absolute; left: 0; width: 560px; top: 592px; text-align: center; font-family: "Open Sans", sans-serif; font-size: 24px; line-height: 30px; text-transform: uppercase; }
  .tagline em { color: var(--gold-mid); }
  .front-band { position: absolute; left: 0; top: 676px; width: 560px; height: 160px; background: linear-gradient(100deg, var(--gold-light) 0%, var(--gold-mid) 70%, var(--gold-deep) 100%); }
  .author-name { position: absolute; left: 0; width: 560px; top: 716px; text-align: center; font-family: "Bebas Neue", sans-serif; font-size: 88px; line-height: 1; color: var(--ink-blue); }
</style>
</head>
<body>
<main class="cover">
  <section class="back">
    <div class="back-title">
      <div class="display" style="top:70px;font-size:58px;">Walking</div>
      <div class="display gold" style="top:115px;font-size:84px;">Into</div>
      <div class="connector" style="top:180px;height:30px;font-size:24px;">
        <span class="rule" style="width:64px;"></span><span style="margin:0 8px;">amber</span><span class="rule right" style="width:64px;"></span>
      </div>
      <div class="display gold" style="top:204px;font-size:104px;">Light</div>
    </div>
    <div class="back-divider"></div>
    <div class="blurb">
      <p>Dicunt percipit deserunt ut usu. Aliquip delenit an eam, vocent vituperata vim ea. Ei mollis audire interpretaris cum, ei impedit fierent sea. Ius at homero noster prompta, ea sit dignissim vituperata efficiendi. Natum placerat ad mei.</p>
      <p>Expetenda tincidunt in sed, ex partem placerat sea, porro commodo ex eam. His putant aeterno interesset at. Usu ea mundi tincidunt, omnium virtute aliquando ius ex. Ea aperiri sententiae duo. Usu nullam dolorum quaestio ei, sit vidit facilisis ea. Per ne impedit iracundia neglegentur. Consetetur neglegentur eum ut, vis animal legimus inimicus id.</p>
      <p>No his munere interesset. At soluta accusam gloriatur eos, ferri commodo sed id, ei tollit legere nec. Eum et iudico graecis, cu zzril instructior per, usu at augue epicurei. Saepe scaevola takimata vix id. Errem dictas posidonium id vis, ne modo affert incorrupte eos.</p>
    </div>
    <div class="back-band"></div>
    <div class="price-panel"></div>
  </section>

  <section class="spine">
    <div class="spine-text spine-title">Walking Into <em>amber</em> Light</div>
    <div class="spine-text spine-author">Author Name</div>
  </section>

  <section class="front">
    <div class="front-title">
      <div class="display" style="top:60px;font-size:126px;">Walking</div>
      <div class="display gold" style="top:160px;font-size:174px;">Into</div>
      <div class="connector" style="top:318px;height:50px;font-size:48px;">
        <span class="rule" style="width:140px;"></span><span style="margin:0 16px;">amber</span><span class="rule right" style="width:140px;"></span>
      </div>
      <div class="display gold" style="top:348px;font-size:226px;">Light</div>
    </div>
    <p class="tagline">Seven Steady Habits to Rise Above<br>Hard Seasons <em>Christian Based</em></p>
    <div class="front-band"></div>
    <div class="author-name">Author Name</div>
  </section>
</main>
</body>
</html>
```